Psychologist website

Simple psychologist website
Site map:
home
self-test
common conditions
children
contact
about
info

Current website:
http://www.moriklepsychology.com.au/

Not in love with logo, or colours etc - open brief
Happy for new font/style/logo for company name

Customer wants clean, credible and warm and friendly look & feel
stock photos OK

Brief:

One home page - simple with 2 or 3 small areas to tease and attract the user and one template page to suit all the other pages

Pages structurally similar to
http://www.quellbyhouse.com.au/
In that the home page is different and the other pages are based on one template

Requirements
Must have
• 2 pages - one home page and one template page
• navigation for site map

```html
<!DOCTYPE html>
<html lang="en">
<head>
<meta charset="utf-8">
<title>Morikle &amp; Associates — Clinical Psychologists</title>
<link href="https://fonts.googleapis.com/css2?family=Questrial&family=PT+Sans&display=swap" rel="stylesheet">
<style>
  :root {
    --sky: #aed4e0;
    --teal: #0f6a80;
    --teal-dark: #0a5566;
    --ink: #1a6c84;
    --nav-text: #a9dbe6;
    --white: #ffffff;
  }
  * { box-sizing: border-box; margin: 0; padding: 0; }
  html, body { width: 1200px; height: 1000px; overflow: hidden; }
  body {
    position: relative;
    background: var(--sky);
    font-family: "Questrial", sans-serif;
    color: var(--ink);
  }

  .search {
    position: absolute; left: 892px; top: 15px; width: 185px; height: 31px;
    background: var(--white); border: 1px solid #7d98a3;
    display: flex; align-items: center; gap: 8px; padding-left: 2px;
    font-size: 15px; color: #6a7c84;
  }
  .search svg { width: 26px; height: 26px; }

  .brand { position: absolute; left: 122px; top: 40px; width: 477px; text-align: right; color: var(--teal-dark); }
  .brand-name { font-size: 40px; letter-spacing: 1px; line-height: 48px; border-bottom: 4px solid #7fa4be; padding-bottom: 2px; }
  .brand-sub { font-size: 24px; letter-spacing: 3px; margin-top: 2px; padding-right: 2px; }

  .tagline {
    position: absolute; left: 612px; top: 66px; width: 430px;
    font-size: 14.5px; line-height: 17px; font-style: italic; color: var(--teal-dark);
  }

  .main-nav {
    position: absolute; left: 120px; top: 136px; width: 960px; height: 56px;
    background: linear-gradient(#137a90, #0c6275 70%, #0a5566);
    border-top: 4px solid #9ec9d6;
    display: flex; align-items: center; justify-content: space-between; padding: 0 34px 0 36px;
  }
  .main-nav a {
    color: var(--nav-text); text-decoration: none; font-size: 24px; letter-spacing: .5px; font-weight: bold;
  }
  .main-nav a.current { color: var(--white); }

  .hero { position: absolute; left: 120px; top: 197px; width: 960px; height: 484px; overflow: hidden; }
  .hero-photo {
    position: absolute; inset: 0;
    background: linear-gradient(90deg, #3a4352 0%, #5b6470 14%, #f3f4f3 30%, #f6f6f5 50%, #2a2d33 60%, #f4f4f2 68%, #e7e8e6 100%);
  }
  .hero-caption {
    position: absolute; left: 0; right: 0; top: 316px; height: 168px;
    background: rgba(20, 22, 24, .68);
    color: var(--white); font-family: "PT Sans", sans-serif; font-size: 21px; line-height: 24px;
    text-align: center; padding: 26px 48px 0;
  }
  .dots { position: absolute; left: 435px; top: 442px; display: flex; gap: 3px; }
  .dots span { width: 17px; height: 17px; border-radius: 50%; border: 2px solid #d8d8d8; }
  .dots span.on { background: #d8d8d8; }

  .panel { position: absolute; background: var(--white); border: 3px solid var(--teal); padding: 6px 12px; }
  .panel h2 { font-weight: normal; font-size: 32px; line-height: 40px; color: var(--ink); }
  .panel p { font-size: 17px; line-height: 19.3px; text-align: justify; text-indent: 30px; }
  .news { left: 121px; top: 698px; width: 291px; height: 248px; }
  .news h2 { margin-bottom: 20px; }
  .more { display: block; text-align: right; font-size: 15px; color: var(--teal-dark); text-decoration: none; }
  .lecture { left: 121px; top: 962px; width: 291px; height: 80px; }
  .welcome { left: 441px; top: 698px; width: 638px; height: 340px; padding: 6px 13px 6px 9px; }
  .welcome h2 { margin-bottom: 22px; }
  .welcome p { margin-bottom: 19px; }
</style>
</head>
<body>
  <div class="search">
    <svg viewBox="0 0 26 26" aria-hidden="true"><circle cx="10" cy="10" r="7.5" fill="none" stroke="#3d5660" stroke-width="2"/><line x1="15.5" y1="15.5" x2="23" y2="23" stroke="#3d5660" stroke-width="3"/></svg>
    Search here...
  </div>

  <header class="brand">
    <div class="brand-name">Morikle &amp; Associates</div>
    <div class="brand-sub">CLINICAL PSYCHOLOGISTS</div>
  </header>

  <p class="tagline">Psychologists, in Sydney, Chatswood,<br>and Westmead. We provide expert treatment for depression, anxiety, eating disorders and other issues.</p>

  <nav class="main-nav">
    <a class="current" href="#">HOME</a>
    <a href="#">SELF-TEST</a>
    <a href="#">COMMON CONDITIONS</a>
    <a href="#">CHILDREN</a>
    <a href="#">ABOUT&nbsp; US</a>
    <a href="#">INFO</a>
  </nav>

  <section class="hero">
    <div class="hero-photo" role="img" aria-label="Stock photo of a therapist taking notes on a clipboard beside a client in a white shirt"></div>
    <div class="hero-caption">“Specialising in cognitive-behaviour therapy (CBT) for adults experiencing difficulties with depression, anxiety, eating disorders, stress, trauma, adjustment to illness or disability, and other common issues”</div>
    <div class="dots"><span class="on"></span><span></span><span></span><span></span><span></span></div>
  </section>

  <aside class="panel news">
    <h2>News</h2>
    <p>ANNOUNCING... A new child, adolescent and family clinic as a sub-group of Morikle and Associates; KIDMINDS HUB. We offer specialist assessment, therapy, training for teachers, school visits. www.kidmindshub.com.au</p>
    <a class="more" href="#">see more...</a>
  </aside>

  <aside class="panel lecture">
    <h2>Latest Lecture</h2>
  </aside>

  <main class="panel welcome">
    <h2>Welcome</h2>
    <p>Our psychologists provide a comfortable, supportive, and confidential environment for their clients. Our first goal is for you to feel comfortable in exploring issues and sharing sharing your concerns, knowing that you have been heard and understood. It is in this kind of environment that client and therapist can work productively to understand problems and seek solutions.</p>
    <p>We emphasise the importance of using techniques that have been demonstrated as effective by independent research. The main therapeutic technique used by our clinicians is Cognitive Behaviour Therapy (CBT).</p>
    <p>Our Psychologists are fully registered and qualified professionals.&nbsp; All are highly trained with Masters or Doctoral degrees in Clinical Psychology and offer</p>
  </main>
</body>
</html>
```